Packiging of mouse trap

We need a packiging for a new mousetrap called 'The Snapwell'. It is a mouse/rat trap. We want to have it pretty simple and modern. The logo of the mouse trap is in the attachment and the measures of the packaging also (don't look at the design, it has nothing to do with us). It's needs to stand out in between the other packaging due to it's simplicity and modern touch.

Font styles to use
Sans Serif

Requirements
Must have
• Simplicity, modern
Should not have
• Too many colors

```html
<!DOCTYPE html>
<html lang="en">
<head>
<meta charset="utf-8">
<title>The Snapwell – Electric Mouse Trap Packaging</title>
<link href="https://fonts.googleapis.com/css2?family=Archivo+Black&family=Exo+2:wght@300;400&family=Cormorant+Garamond:wght@500&family=Montserrat:wght@500&display=swap" rel="stylesheet">
<style>
  :root {
    --bg: #e4e4e4;
    --mint: #b2d89a;
    --mint-deep: #9cc884;
    --ink: #1b1c1c;
    --paper: #ffffff;
    --tag-text: #a6d08c;
    --soft-line: #9a9a9a;
  }
  * { box-sizing: border-box; margin: 0; padding: 0; }
  html, body {
    width: 1200px; height: 960px; overflow: hidden;
    background: var(--bg);
  }
  .canvas {
    position: relative; width: 1200px; height: 960px;
    display: flex; align-items: center; justify-content: center;
  }
  .panel {
    position: relative; width: 344px; height: 884px;
    background: var(--ink); overflow: hidden;
  }
  .panel__pattern {
    position: absolute; left: 0; top: 0; width: 100%; height: 540px;
    background: linear-gradient(160deg, var(--mint) 0%, var(--mint-deep) 100%);
  }
  .claim-tag {
    position: absolute; left: 130px; top: 38px; width: 92px;
  }
  .claim-tag svg { display: block; }
  .claim-tag__text {
    position: absolute; left: 0; top: 10px; width: 100%;
    text-align: center; font-family: "Montserrat", sans-serif; font-weight: 500;
    color: var(--tag-text); font-size: 11.5px; line-height: 1.25; letter-spacing: 0.02em;
  }
  .claim-tag__rule {
    width: 64px; height: 1px; background: var(--tag-text); margin: 4px auto 5px;
  }
  .vertical-line {
    position: absolute; left: 172px; top: 160px; width: 14px;
    font-family: "Cormorant Garamond", serif; font-weight: 500;
    font-size: 14px; line-height: 17.5px; color: var(--ink);
    text-align: center; transform: translateX(-50%);
  }
  .brand-name {
    position: absolute; left: 0; width: 100%; bottom: 344px;
    font-family: "Archivo Black", sans-serif; font-size: 52px; line-height: 0.92;
    color: var(--ink); text-align: center; text-transform: uppercase; letter-spacing: -0.02em;
  }
  .product-type {
    position: absolute; left: 0; width: 100%; top: 585px;
    text-align: center; font-family: "Exo 2", sans-serif; font-weight: 400;
    color: var(--paper); font-size: 17px; line-height: 40px; letter-spacing: 0.01em;
  }
  .features {
    position: absolute; left: 30px; top: 712px; width: 284px; height: 96px;
  }
  .features__grid { position: absolute; inset: 0; }
  .feature {
    position: absolute; display: flex; align-items: center; gap: 9px;
    font-family: "Exo 2", sans-serif; font-weight: 300; color: var(--paper); font-size: 14px;
  }
  .feature svg { flex: none; }
  .feature--easy { left: 0; top: 8px; }
  .feature--reusable { left: 152px; top: 2px; }
  .feature--safe { left: 0; top: 56px; }
  .feature--power { left: 152px; top: 50px; }
  .website {
    position: absolute; left: 0; width: 100%; top: 845px;
    text-align: center; font-family: "Exo 2", sans-serif; font-weight: 300;
    color: var(--paper); font-size: 9.5px; letter-spacing: 0.02em;
  }
</style>
</head>
<body>
<main class="canvas">
  <section class="panel">
    <div class="panel__pattern" role="img" aria-label="Light green circuit-line pattern with faint silhouettes of mice being zapped"></div>

    <div class="claim-tag">
      <svg width="92" height="97" viewBox="0 0 92 97">
        <polygon points="0,0 92,0 92,97 46,80 0,97" fill="var(--paper)"/>
      </svg>
      <div class="claim-tag__text">
        INSTANT<br>KILL TRAP
        <div class="claim-tag__rule"></div>
        PET SAFE
      </div>
    </div>

    <div class="vertical-line">L<br>o<br>r<br>e<br>m<br><br>i<br>p<br>s<br>u<br>m</div>

    <h1 class="brand-name">The<br>Snapwell</h1>

    <p class="product-type">ELECTRIC<br>MOUSE TRAP</p>

    <div class="features">
      <svg class="features__grid" width="284" height="96" viewBox="0 0 284 96">
        <line x1="0" y1="48" x2="276" y2="42" stroke="var(--soft-line)" stroke-width="1"/>
        <line x1="142" y1="0" x2="142" y2="96" stroke="var(--soft-line)" stroke-width="1"/>
      </svg>
      <div class="feature feature--easy">
        <svg width="30" height="30" viewBox="0 0 30 30"><circle cx="15" cy="15" r="13" fill="none" stroke="#fff" stroke-width="2"/><polyline points="9,15 13,20 21,10" fill="none" stroke="#fff" stroke-width="2"/></svg>
        Easy to use
      </div>
      <div class="feature feature--reusable">
        <svg width="30" height="30" viewBox="0 0 30 30"><circle cx="15" cy="15" r="13" fill="none" stroke="#fff" stroke-width="2"/><path d="M9 13a6.5 6.5 0 0 1 11.5-2.5M21 17a6.5 6.5 0 0 1-11.5 2.5" fill="none" stroke="#fff" stroke-width="2"/><polyline points="21,7 21,11 17,11" fill="none" stroke="#fff" stroke-width="1.6"/><polyline points="9,23 9,19 13,19" fill="none" stroke="#fff" stroke-width="1.6"/></svg>
        Reusable
      </div>
      <div class="feature feature--safe">
        <svg width="30" height="30" viewBox="0 0 30 30"><circle cx="15" cy="15" r="13" fill="none" stroke="#fff" stroke-width="2"/><rect x="8" y="11" width="14" height="8" rx="4" fill="none" stroke="#fff" stroke-width="1.8"/><line x1="15" y1="11" x2="15" y2="19" stroke="#fff" stroke-width="1.5"/></svg>
        No Injuries
      </div>
      <div class="feature feature--power">
        <svg width="30" height="30" viewBox="0 0 30 30"><circle cx="15" cy="15" r="13" fill="none" stroke="#fff" stroke-width="2"/><polygon points="16,6 10,16 14,16 13,24 20,13 16,13" fill="#fff"/></svg>
        Powerful
      </div>
    </div>

    <p class="website">WWW.SNAPWELLHOME.COM</p>
  </section>
</main>
</body>
</html>
```